Lantern Business Cards

Need business cards for my employees at my restaurant.

Needs to include:
Our Logo
Lantern Bowls & Brews
Name: Nora Pettigrew
Title : Owner
Address: 487 Mirella Ave. Kestrel Point, WL 86519
Web: www.lanternkestrel.com
Phone: 555-210-0147
Cell: 555-210-0192
Email: info@lanternkestrel.com

```html
<!DOCTYPE html>
<html lang="en">
<head>
<meta charset="utf-8">
<title>Lantern Bowls &amp; Brews – Business Card</title>
<link href="https://fonts.googleapis.com/css2?family=Open+Sans:wght@400;600;700&display=swap" rel="stylesheet">
<style>
  :root {
    --stage: #2f2f31;
    --brand-red: #c0182b;
    --brand-red-deep: #7e0a17;
    --brand-red-mid: #a5111f;
    --ink: #3a3a3a;
    --ink-soft: #555;
    --paper: #ffffff;
    --paper-shade: #ececec;
    --rule: #2b2b2b;
    --ghost: #ececec;
  }
  * { margin: 0; padding: 0; box-sizing: border-box; }
  html, body { width: 1200px; height: 900px; overflow: hidden; }
  body {
    background: var(--stage);
    font-family: "Open Sans", Arial, sans-serif;
    position: relative;
  }
  .card {
    position: absolute;
    width: 640px;
    height: 366px;
    border-radius: 28px;
    overflow: hidden;
    box-shadow: 0 18px 40px rgba(0,0,0,.45);
  }
  /* back side */
  .card-back {
    left: 90px; top: 60px;
    background: var(--brand-red-mid);
  }
  .back-pattern {
    position: absolute; inset: 0;
    background: radial-gradient(ellipse at 50% 50%, var(--brand-red) 0%, var(--brand-red-mid) 55%, var(--brand-red-deep) 100%);
  }
  .back-mark {
    position: absolute;
    right: 70px; top: 150px;
    display: flex; align-items: center; gap: 8px;
    color: var(--paper);
    font-weight: 700;
    font-size: 22px;
    letter-spacing: 1px;
  }
  .back-mark .dot {
    width: 14px; height: 14px; border-radius: 50%; background: var(--paper);
  }
  /* front side */
  .card-front {
    left: 470px; top: 480px;
    background: linear-gradient(120deg, var(--paper-shade) 0%, var(--paper) 45%, var(--paper) 100%);
  }
  .ghost-mark {
    position: absolute;
    right: 40px; top: 10px;
    font-weight: 700;
    font-size: 100px;
    line-height: 1.2;
    color: var(--ghost);
    letter-spacing: 2px;
  }
  .brand {
    position: absolute;
    left: 36px; top: 140px;
    width: 244px;
  }
  .brand-name {
    display: flex; align-items: center; gap: 10px;
    color: var(--brand-red);
    font-weight: 700;
    font-size: 40px;
    line-height: 1;
    letter-spacing: 1px;
    text-transform: uppercase;
  }
  .brand-name .square { width: 16px; height: 16px; background: var(--brand-red); }
  .brand-tagline {
    display: flex; align-items: center; gap: 8px;
    margin-top: 8px;
    font-size: 11px;
    font-weight: 600;
    color: var(--rule);
    letter-spacing: .5px;
    text-transform: uppercase;
  }
  .brand-tagline::before, .brand-tagline::after {
    content: ""; flex: 1; height: 1px; background: var(--rule);
  }
  .person {
    position: absolute;
    right: 352px; top: 222px;
    text-align: right;
    line-height: 1.3;
  }
  .person-title { font-size: 16px; color: var(--ink-soft); }
  .person-name {
    font-size: 17px; font-weight: 700; color: var(--brand-red);
    text-transform: uppercase; letter-spacing: .5px;
  }
  .divider {
    position: absolute;
    left: 300px; top: 148px;
    width: 1.5px; height: 120px;
    background: var(--rule);
  }
  .contacts {
    position: absolute;
    left: 314px; top: 148px;
    list-style: none;
    font-size: 14px;
    color: var(--ink);
    line-height: 1.5;
  }
  .contacts li { display: flex; align-items: center; gap: 8px; }
  .contacts svg { width: 14px; height: 14px; flex: none; }
  .contacts .address { padding-left: 22px; display: block; }
</style>
</head>
<body>
  <section class="card card-back" aria-label="Card back">
    <div class="back-pattern" role="img" aria-label="Embossed repeating brand pattern in deep red"></div>
    <div class="back-mark"><span class="dot"></span>Lantern</div>
  </section>

  <section class="card card-front" aria-label="Card front">
    <div class="ghost-mark" aria-hidden="true">Lantern</div>

    <div class="brand">
      <div class="brand-name"><span class="square"></span>Lantern</div>
      <div class="brand-tagline">Bowls &amp; Brews</div>
    </div>

    <div class="person">
      <p class="person-title">Owner</p>
      <p class="person-name">Nora Pettigrew</p>
    </div>

    <div class="divider"></div>

    <ul class="contacts">
      <li>
        <svg viewBox="0 0 16 16" fill="none" stroke="#c0182b" stroke-width="1.6"><rect x="4" y="1" width="8" height="14" rx="1.5"/><line x1="7" y1="12.5" x2="9" y2="12.5"/></svg>
        555-210-0192
      </li>
      <li>
        <svg viewBox="0 0 16 16" fill="#c0182b"><path d="M3 1.5l2.5-.5 1.5 3.5-1.8 1.2c.8 1.8 2.3 3.3 4.1 4.1L10.5 8 14 9.5l-.5 2.5c-.3 1-1.3 1.6-2.3 1.4C6.5 12.6 3.4 9.5 2.6 4.8 2.4 3.8 2 2 3 1.5z"/></svg>
        555-210-0147
      </li>
      <li>
        <svg viewBox="0 0 16 16" fill="#c0182b"><path d="M1 3h14v10H1z"/><path d="M1 3l7 5 7-5" stroke="#fff" stroke-width="1.3" fill="none"/></svg>
        info@lanternkestrel.com
      </li>
      <li>
        <svg viewBox="0 0 16 16" fill="none" stroke="#c0182b" stroke-width="1.3"><circle cx="8" cy="8" r="6.5"/><ellipse cx="8" cy="8" rx="3" ry="6.5"/><line x1="1.5" y1="8" x2="14.5" y2="8"/></svg>
        www.lanternkestrel.com
      </li>
      <li class="address">487 Mirella Ave.<br>Kestrel Point, WL 86519</li>
    </ul>
  </section>
</body>
</html>
```